Brenwold Brochure

We need a professional corporate brochure - printed on 4 sides (cover, 2 inside pages & back page) to promote and generate interest about Brenwold Consultancy and its services offered.

Brenwold Consultancy is a boutique management consultancy company focused exclusively on revenue generation for businesses. We advise companies on specific ways to increase revenue. We assess the revenue generation strategy, resolve revenue generation issues and generate revenue growth opportunities.
"Revenue Growth Built From The Inside Out!"

The brochure needs to focus on sales and our unique selling proposition - that we can offer the entire package - Training, Sales Systems , Sales Force Effectiveness, Sales Manager Coaching, etc.

Target audience in Business owners and General Managers.

The feel of the brochure needs to be clean lines , corporate image and professional
Updates

Reason: Guys Designs are still dribbling in - so have extended 3 days Cheers Dmitri

Target Market(s)

Business Owners
CEOS
General Managers

Requirements
Must have
• 1. Corporate logo - refer attached (Brenwold Business Cards Art)
• 2. List of Service offered - refer attached (Brenwold Services)
• 3. Process Steps wheel - refer attached ( Process Steps)
• 4. About us:
• Brenwold is a boutique management consultancy company focused exclusively on revenue generation for small businesses. We advise companies on specific ways to increase revenue. We assess the revenue generation strategy, resolve revenue generation issues and generate revenue growth opportunities.
• Revenue Growth Built From The Inside Out!
• 5. Why Brenwold Consultancy
• Our experience in profit improvement strategies can provide you with an independent perspective of your organisation and identify opportunities to fine tune your sales and marketing operations, while gaining a sustainable competitive advantage. Companies that optimise their sales systems and marketing efforts to win in today’s economic conditions will expand their market share and competitive position during the current economic downturn.
• 6. The Process We Follow
• Analysis of your current market
• Understand your business objectives
• Your key Strategies
• Review current steps to achieving your objectives
• Investigate programs and their budget impact
• Schedules and assignments
• 7. What will we do:
• The Brenwold team is passionate about adding value to our customers business. We will bring our expertise and experience to ensure we add value to your business. The team will always maintain a high level of professionalism and confidentiality throughout all our dealings, as we are committed to the highest standards.
• We will review your company’s processes, audience, existing materials and the market. Brenwold will then produce a report that covers all findings and recommendations.
• 8. Company Name , ABN number , Tel number and email address refer attached (with list of services)
• :
Nice to have
• Sales images / Corporate revenue images / diagrams etc.

```html
<!DOCTYPE html>
<html lang="en">
<head>
<meta charset="utf-8">
<title>Brenwold Consultancy Brochure</title>
<link rel="stylesheet" href="https://fonts.googleapis.com/css2?family=Arimo:wght@400;700&display=swap">
<style>
  :root {
    --stage: #e4e4e6;
    --stage-edge: #c9c9cc;
    --page-deep: #2b2d3d;
    --page-mid: #4a4d66;
    --page-light: #7d8099;
    --glow: #dfe3ee;
    --service-text: #a9c4ea;
    --ink-light: #ffffff;
    --ink-dark: #1b1d2a;
    --brand-blue: #3b6fc6;
  }
  * { margin: 0; padding: 0; box-sizing: border-box; }
  html, body { width: 1200px; height: 833px; overflow: hidden; }
  body {
    background: radial-gradient(ellipse at 50% 40%, var(--stage) 0%, var(--stage-edge) 100%);
    font-family: "Arimo", Arial, sans-serif;
    position: relative;
  }
  .page {
    position: absolute;
    top: 66px;
    width: 495px;
    height: 700px;
    overflow: hidden;
    box-shadow: 0 10px 28px rgba(0,0,0,0.28);
  }
  .page--back { left: 85px; }
  .page--cover { left: 620px; }

  .page-backdrop {
    position: absolute; inset: 0;
    background:
      radial-gradient(circle at 70% 30%, rgba(160,165,195,0.35) 0%, transparent 45%),
      radial-gradient(circle at 20% 80%, rgba(120,125,160,0.3) 0%, transparent 40%),
      linear-gradient(160deg, var(--page-mid) 0%, var(--page-deep) 100%);
  }
  .cover-photo {
    position: absolute; inset: 0;
    background:
      radial-gradient(circle at 38% 40%, var(--glow) 0%, rgba(200,205,222,0.75) 14%, rgba(120,125,155,0.4) 30%, transparent 48%),
      radial-gradient(ellipse at 80% 55%, rgba(25,25,35,0.85) 0%, rgba(25,25,35,0.5) 30%, transparent 55%),
      linear-gradient(160deg, var(--page-light) 0%, var(--page-mid) 45%, var(--page-deep) 100%);
  }

  .service-list {
    position: absolute;
    left: 46px; top: 110px;
    width: 250px;
    list-style: none;
    color: var(--service-text);
    font-size: 11px;
    line-height: 1.3;
  }
  .service-list li { margin-bottom: 9px; }

  .back-brand {
    position: absolute;
    left: 46px; top: 520px;
    color: var(--ink-light);
  }
  .brand-mark {
    display: flex; align-items: center; gap: 8px;
  }
  .brand-dot {
    flex: none;
    width: 20px; height: 20px; border-radius: 50%;
    background: var(--ink-light);
  }
  .back-brand .brand-name { font-weight: 700; font-size: 15px; }
  .back-brand .brand-tagline { font-size: 7px; margin: 3px 0 0 28px; }
  .contact-details {
    margin-top: 16px;
    font-size: 10px; font-weight: 700; line-height: 1.35;
  }

  .cover-brand {
    position: absolute;
    left: 110px; top: 240px;
    color: var(--ink-dark);
  }
  .cover-brand .brand-dot {
    width: 40px; height: 40px;
    background: var(--brand-blue);
  }
  .cover-brand .brand-name { font-weight: 700; font-size: 24px; white-space: nowrap; }
  .cover-brand .brand-tagline {
    font-weight: 700; font-size: 10px; margin: 4px 0 0 48px;
  }
  .cover-web {
    position: absolute;
    right: 36px; bottom: 58px;
    color: var(--ink-light);
    font-weight: 700; font-size: 17px;
  }
</style>
</head>
<body>
  <section class="page page--back">
    <div class="page-backdrop" role="img" aria-label="Abstract dark blue-grey technology graphic with soft light circles"></div>
    <ul class="service-list">
      <li>Marketing support</li>
      <li>Sales Strategy assessment and development – compare to best practice and identify opportunities for improvement</li>
      <li>Sales effectiveness to increase efficiency</li>
      <li>Review of sales structures</li>
      <li>Development of target lists, competitor lists and market share analysis – maximise your sales channels</li>
      <li>Assessment of structure of compensation plans, quotas, and territories</li>
      <li>Advice on how to transition to a value focused process centred, milestone based sales organisation</li>
      <li>Deployment of software and hardware to improve productivity</li>
      <li>Pipe Line Management and Forecasting</li>
      <li>One on One Coaching/Tender / Presentation support</li>
    </ul>
    <div class="back-brand">
      <div class="brand-mark">
        <span class="brand-dot"></span>
        <span class="brand-name">Brenwold Consultancy</span>
      </div>
      <p class="brand-tagline">Revenue Growth Built From The Inside Out</p>
      <p class="contact-details">
        ABN 47 260 315 418<br>
        admin@brenwoldconsultancy.com.au<br>
        Tel: 1300 482 615
      </p>
    </div>
  </section>

  <section class="page page--cover">
    <div class="cover-photo" role="img" aria-label="Photo of a businessman in a dark suit touching a glowing digital interface"></div>
    <div class="cover-brand">
      <div class="brand-mark">
        <span class="brand-dot"></span>
        <span class="brand-name">Brenwold Consultancy</span>
      </div>
      <p class="brand-tagline">Revenue Growth Built From The Inside Out</p>
    </div>
    <p class="cover-web">www.brenwoldconsultancy.com.au</p>
  </section>
</body>
</html>
```